Personalized Technology Company Needs a Business Card

I need a double-sided business card. Both sides will have the logo, and the contact information. One side will be black, with the white / gray logo, and the other will be white, with the black / gray logo. The black side will have the text "Custom Gaming PC's" and will have a water-cooled gaming PC image. The white side will have the text "Custom Business Computers & Consulting", and will have a business / enterprise PC image. Feel free to add a conservative image in the background, while the color remains unchanged. I'm uploading the base logo (transparent), so you can modify the colors, both the finished colored logos and an idea of ​​the business card (with the current information, just missing the website, which is www.velmorisystems.com, please add it.) Thank you so much for your effort, I'll be specting your cool designs. Good Luck!

Target Market(s)

Gamers & Entrepreneurs / Business Owners / Chief Technology Officers

Industry/Entity Type

Technology Equipment

Contact Information for Business Card

I need a double-sided business card. Both sides will have the logo, and the contact information. One side will be black, with the white/gray logo, and the other one will be white, with the black/gray logo. The black side will have the text "Custom Gaming PC's" and will have a water-cooled gaming PC image. The white side will have the text "Custom Business Computers & Consulting", and will have a business/enterprise PC image. Feel free to add a conservative image in the background, whilst the color remains unchanged.

I'm uploading the base logo (transparent), so you can modify the colors, both the finished colored logos and an idea of the business card (with the actual information, just missing the website, which is www.velmorisystems.com, please add it.)

Thank you so much for your effort, I'll be specting your cool designs. Good Luck!

Font styles to use
Serif

Colors
000000
757575
ffffff

Requirements
Must have
• Please See Description
Nice to have
• Please See Description
Should not have
• Please See Description

```html
<!DOCTYPE html>
<html lang="en">
<head>
<meta charset="utf-8">
<title>Velmori Systems — Business Cards</title>
<link rel="stylesheet" href="https://fonts.googleapis.com/css2?family=Tinos:wght@400;700&display=swap">
<style>
  :root {
    --black: #000000;
    --grey: #757575;
    --white: #ffffff;
    --cream: #ece6da;
    --accent: #2a8fd8;
    --stage: #1c1c1f;
    --ink-dark: #111111;
  }
  * { margin: 0; padding: 0; box-sizing: border-box; }
  html, body { width: 1200px; height: 800px; overflow: hidden; }
  body {
    background: var(--stage);
    font-family: "Tinos", "Times New Roman", serif;
    position: relative;
  }
  .card {
    position: absolute;
    left: 280px;
    width: 640px;
    height: 366px;
    overflow: hidden;
  }
  .card--gaming { top: 22px; background: var(--black); color: var(--white); }
  .card--business { top: 410px; background: var(--white); color: var(--ink-dark); }

  .card__visual { position: absolute; right: 0; top: 0; width: 380px; height: 322px; }

  .card__band {
    position: absolute; left: 0; bottom: 0; width: 100%; height: 44px;
    display: flex; align-items: center; padding-left: 34px;
    font-size: 17px; letter-spacing: 1.5px; text-transform: uppercase;
  }
  .card--gaming .card__band { background: var(--cream); color: var(--ink-dark); }
  .card--business .card__band { background: var(--black); color: var(--white); }

  .brand {
    position: absolute; left: 44px; top: 54px;
    display: flex; align-items: center; gap: 14px;
  }
  .brand__mark { width: 46px; height: 46px; background: var(--grey); }
  .brand__name {
    font-size: 30px; font-weight: 400; letter-spacing: 5px; line-height: 1.05;
    text-transform: uppercase;
  }
  .card--gaming .brand__name { color: var(--white); }
  .card--business .brand__name { color: var(--black); }
  .brand__name span { display: block; font-size: 14px; letter-spacing: 6px; }

  .person { position: absolute; left: 58px; top: 150px; }
  .person__name { font-size: 22px; font-weight: 700; }
  .person__title { font-size: 16px; color: var(--accent); }
  .person__accent {
    position: absolute; left: -30px; top: 34px; width: 0; height: 0;
    border-top: 10px solid transparent; border-bottom: 10px solid transparent;
    border-left: 14px solid var(--accent);
  }

  .contacts { position: absolute; left: 58px; top: 212px; font-size: 14px; }
  .contacts__group { display: flex; align-items: center; gap: 10px; }
  .contacts__icons { display: flex; flex-direction: column; gap: 3px; }
  .icon { width: 16px; height: 16px; display: block; }
  .contacts__divider {
    width: 250px; margin: 8px 0 8px 22px;
    border-top: 2px dotted var(--grey);
  }
  .contacts__lines { line-height: 1.35; }
</style>
</head>
<body>

<!-- Black side -->
<section class="card card--gaming">
  <svg class="card__visual" viewBox="0 0 380 322" role="img" aria-label="Water-cooled gaming PC interior with blue coolant tubes">
    <defs>
      <linearGradient id="gamingTone" x1="0" y1="0" x2="1" y2="1">
        <stop offset="0" stop-color="#3a7fe0"/>
        <stop offset="0.5" stop-color="#1b3f8f"/>
        <stop offset="1" stop-color="#0b1840"/>
      </linearGradient>
    </defs>
    <path fill="url(#gamingTone)" d="M380 0 H150 L140 20 L160 38 L128 60 L150 84 L118 110 L144 132 L110 158 L138 182 L104 206 L132 228 L100 252 L128 276 L96 300 L120 322 H380 Z"/>
  </svg>

  <div class="brand">
    <div class="brand__mark"></div>
    <div class="brand__name">Velmori<span>Systems</span></div>
  </div>

  <div class="person">
    <span class="person__accent"></span>
    <div class="person__name">Daniel Ruiz Marden</div>
    <div class="person__title">(CEO &amp; Co-Founder)</div>
  </div>

  <div class="contacts">
    <div class="contacts__group">
      <div class="contacts__icons">
        <svg class="icon" viewBox="0 0 16 16"><rect width="16" height="16" fill="var(--accent)"/><path d="M5 3 L7 5 L6 7 Q7 9 9 10 L11 9 L13 11 L11 13 Q6 12 3 5 Z" fill="var(--white)"/></svg>
        <svg class="icon" viewBox="0 0 16 16"><rect width="16" height="16" fill="var(--accent)"/><rect x="5" y="3" width="6" height="10" rx="1" fill="var(--white)"/></svg>
      </div>
      <div class="contacts__lines">+52 5812 - 3307<br>+52 55 - 4819 - 6053</div>
    </div>
    <div class="contacts__divider"></div>
    <div class="contacts__group">
      <div class="contacts__icons">
        <svg class="icon" viewBox="0 0 16 16"><rect width="16" height="16" fill="var(--accent)"/><rect x="3" y="5" width="10" height="7" fill="var(--white)"/><path d="M3 5 L8 9 L13 5" stroke="var(--accent)" fill="none"/></svg>
        <svg class="icon" viewBox="0 0 16 16"><rect width="16" height="16" fill="var(--accent)"/><circle cx="8" cy="8" r="5" fill="none" stroke="var(--white)" stroke-width="1.3"/><path d="M3 8 H13 M8 3 Q5 8 8 13 M8 3 Q11 8 8 13" stroke="var(--white)" fill="none"/></svg>
      </div>
      <div class="contacts__lines">contact@velmorisystems.com<br>www.velmorisystems.com</div>
    </div>
  </div>

  <div class="card__band">Custom Gaming PC's</div>
</section>

<!-- White side -->
<section class="card card--business">
  <svg class="card__visual" viewBox="0 0 380 322" role="img" aria-label="Enterprise server room with illuminated rack equipment">
    <defs>
      <linearGradient id="businessTone" x1="0" y1="1" x2="1" y2="0">
        <stop offset="0" stop-color="#0a1030"/>
        <stop offset="0.55" stop-color="#1f4fa8"/>
        <stop offset="1" stop-color="#7fd0f5"/>
      </linearGradient>
    </defs>
    <path fill="url(#businessTone)" d="M380 0 H120 L132 22 L110 46 L138 70 L114 96 L146 120 L120 146 L150 172 L124 198 L156 222 L132 248 L166 272 L146 298 L170 322 H380 Z"/>
  </svg>

  <div class="brand">
    <div class="brand__mark"></div>
    <div class="brand__name">Velmori<span>Systems</span></div>
  </div>

  <div class="person">
    <span class="person__accent"></span>
    <div class="person__name">Daniel Ruiz Marden</div>
    <div class="person__title">(CEO &amp; Co-Founder)</div>
  </div>

  <div class="contacts">
    <div class="contacts__group">
      <div class="contacts__icons">
        <svg class="icon" viewBox="0 0 16 16"><rect width="16" height="16" fill="var(--accent)"/><path d="M5 3 L7 5 L6 7 Q7 9 9 10 L11 9 L13 11 L11 13 Q6 12 3 5 Z" fill="var(--white)"/></svg>
        <svg class="icon" viewBox="0 0 16 16"><rect width="16" height="16" fill="var(--accent)"/><rect x="5" y="3" width="6" height="10" rx="1" fill="var(--white)"/></svg>
      </div>
      <div class="contacts__lines">+52 5812 - 3307<br>+52 55 - 4819 - 6053</div>
    </div>
    <div class="contacts__divider"></div>
    <div class="contacts__group">
      <div class="contacts__icons">
        <svg class="icon" viewBox="0 0 16 16"><rect width="16" height="16" fill="var(--accent)"/><rect x="3" y="5" width="10" height="7" fill="var(--white)"/><path d="M3 5 L8 9 L13 5" stroke="var(--accent)" fill="none"/></svg>
        <svg class="icon" viewBox="0 0 16 16"><rect width="16" height="16" fill="var(--accent)"/><circle cx="8" cy="8" r="5" fill="none" stroke="var(--white)" stroke-width="1.3"/><path d="M3 8 H13 M8 3 Q5 8 8 13 M8 3 Q11 8 8 13" stroke="var(--white)" fill="none"/></svg>
      </div>
      <div class="contacts__lines">contact@velmorisystems.com<br>www.velmorisystems.com</div>
    </div>
  </div>

  <div class="card__band">Custom Business Computers &amp; Consulting</div>
</section>

</body>
</html>
```